Consulting Firm of Business Savvy Super Geeks Needs Business Cards Redesigned

We need our business cards redesigned to reflect the company branding better, especially the website: www.TrelvoAdvisory.com . Note the phrase "Business Savvy. Technology Smart" from the website. Also would love to see options that include verbiage of our offerings: Cloud Solutions, Digital Workspace, CRM Services, Quandrel Partner, Security Services, ERP Services.

Industry/Entity Type

Consulting

Contact Information for Business Card

Direct Phone #, Cell Phone #, Linkedin Address, Web address, Office Address

Font styles to use
Sans Serif

Requirements
Must have
• The cards should reflect the website.
• Clean design.
Nice to have
• Mentions to each of the business units / practices mentioned in the description.

```html
<!DOCTYPE html>
<html lang="en">
<head>
<meta charset="utf-8">
<title>Trelvo Advisory Business Cards</title>
<link href="https://fonts.googleapis.com/css2?family=Arimo:wght@400;700&display=swap" rel="stylesheet">
<style>
  :root {
    --stage: #2b2b2d;
    --card: #f7f8f9;
    --brand-blue: #1d6fb8;
    --brand-light: #4aa3de;
    --slate: #2f4a5c;
    --ink: #1e2328;
    --muted: #7d858c;
  }
  * { box-sizing: border-box; margin: 0; padding: 0; }
  html, body { width: 1200px; height: 997px; overflow: hidden; }
  body {
    background: var(--stage);
    font-family: 'Arimo', Arial, sans-serif;
    position: relative;
  }
  .card {
    position: absolute;
    left: 250px;
    width: 700px;
    height: 400px;
    background: var(--card);
    overflow: hidden;
  }
  .card--back { top: 60px; }
  .card--front { top: 520px; }

  .band {
    position: absolute;
    left: 0; right: 0; bottom: 0;
    height: 44px;
    background: var(--brand-blue);
    color: #fff;
    font-weight: 700;
    display: flex; align-items: center; justify-content: center;
  }
  .band--tagline { font-size: 15px; letter-spacing: 1.5px; }
  .band--web { font-size: 17px; letter-spacing: 4px; }

  /* back card */
  .centre-mark {
    position: absolute;
    left: 50%; top: 150px;
    transform: translateX(-50%);
    display: flex; align-items: center; gap: 14px;
    font-size: 58px; font-weight: 700; color: var(--brand-blue);
  }
  .centre-mark .square { width: 34px; height: 34px; background: var(--brand-light); }
  .service {
    position: absolute;
    font-size: 13px; font-weight: 700; letter-spacing: 0.8px;
    color: var(--muted); text-transform: uppercase;
    display: flex; align-items: center; gap: 7px;
  }
  .service::before {
    content: ""; width: 6px; height: 6px; border-radius: 50%;
    background: var(--brand-light);
  }
  .service--workspace { left: 200px; top: 80px; }
  .service--erp { left: 470px; top: 60px; }
  .service--partner { left: 60px; top: 180px; }
  .service--crm { left: 540px; top: 180px; }
  .service--cloud { left: 110px; top: 290px; }
  .service--security { left: 400px; top: 290px; }

  /* front card */
  .wordmark {
    position: absolute; left: 210px; top: 46px;
    display: flex; align-items: flex-start; gap: 10px;
    font-size: 96px; font-weight: 700; color: var(--slate); line-height: 1;
  }
  .wordmark .square { width: 26px; height: 26px; background: var(--brand-light); margin-top: 4px; }
  .contacts {
    position: absolute; right: 40px; top: 156px;
    text-align: right; font-size: 13px; color: var(--ink);
    list-style: none;
  }
  .contacts li {
    display: flex; justify-content: flex-end;
    align-items: center; gap: 8px; height: 22px;
  }
  .contacts li.rule { height: 2px; background: var(--brand-blue); margin: 4px 0 4px auto; width: 260px; }
  .icon { width: 14px; height: 14px; }
  .divider {
    position: absolute; left: 40px; right: 40px; top: 266px;
    height: 2px; background: var(--brand-blue);
  }
  .person { position: absolute; left: 40px; top: 230px; }
  .person__name { font-size: 20px; font-weight: 700; color: var(--brand-blue); letter-spacing: 0.5px; line-height: 23px; }
  .person__role { font-size: 13px; color: var(--ink); margin-top: 20px; }
  .address {
    position: absolute; left: 40px; top: 302px;
    font-size: 15px; color: var(--brand-blue); line-height: 1.35; font-style: normal;
  }
</style>
</head>
<body>
  <section class="card card--back" aria-label="Card back">
    <div class="centre-mark"><span>Trelvo</span><span class="square"></span></div>
    <span class="service service--workspace">Digital Workspace</span>
    <span class="service service--erp">ERP Services</span>
    <span class="service service--partner">Quandrel Partner</span>
    <span class="service service--crm">CRM Services</span>
    <span class="service service--cloud">Cloud Solutions</span>
    <span class="service service--security">Security Services</span>
    <div class="band band--tagline">BUSINESS SAVVY TECHNOLOGY SMART</div>
  </section>

  <section class="card card--front" aria-label="Card front">
    <div class="wordmark"><span>Trelvo</span><span class="square"></span></div>
    <ul class="contacts">
      <li>555-310-4827
        <svg class="icon" viewBox="0 0 14 14"><circle cx="7" cy="7" r="7" fill="#1d6fb8"/><path d="M4 5.2c0-.8 1.4-1.4 3-1.4s3 .6 3 1.4v.8H8.6v-.6H5.4v.6H4zM4.6 7h4.8l.6 3H4z" fill="#fff"/></svg></li>
      <li>dana.whitlock@trelvoadvisory.com
        <svg class="icon" viewBox="0 0 14 14"><circle cx="7" cy="7" r="7" fill="#1d6fb8"/><rect x="3.5" y="4.5" width="7" height="5" fill="none" stroke="#fff"/><path d="M3.5 4.5 7 7.3l3.5-2.8" fill="none" stroke="#fff"/></svg></li>
      <li class="rule" aria-hidden="true"></li>
      <li>555-310-9054
        <svg class="icon" viewBox="0 0 14 14"><circle cx="7" cy="7" r="7" fill="#1d6fb8"/><path d="M4 5.2c0-.8 1.4-1.4 3-1.4s3 .6 3 1.4v.8H8.6v-.6H5.4v.6H4zM4.6 7h4.8l.6 3H4z" fill="#fff"/></svg></li>
      <li>555-310-2261
        <svg class="icon" viewBox="0 0 14 14"><circle cx="7" cy="7" r="7" fill="#1d6fb8"/><path d="M4 5.2c0-.8 1.4-1.4 3-1.4s3 .6 3 1.4v.8H8.6v-.6H5.4v.6H4zM4.6 7h4.8l.6 3H4z" fill="#fff"/></svg></li>
    </ul>
    <div class="person">
      <div class="person__name">DANA WHITLOCK</div>
      <div class="person__role">CEO</div>
    </div>
    <div class="divider"></div>
    <address class="address">218 Orchard Lane,<br>Millbrook, PA 15990</address>
    <div class="band band--web">WWW.TRELVOADVISORY.COM</div>
  </section>
</body>
</html>
```